Chic streamline modern edgy! Danemerecurls.com

I need a website built for my personal business. I am a hair stylist and I would like a crisp website that works well, is sleek, easy to use, and allows my clients to navigate through Services and pay deposits for services listed.

My logo is somewhat of a full moon, so my theme is nocturnal.

My information can be found at chairbook.com/danemerecurls

Target Market(s)

Women ages 25-55 who are looking for luxury hair extension services

Industry/Entity Type

Hair And Beauty

Number of Pages Required

1 page

Colors
474747
919191
d3d3d3
000000

Requirements
Must have
• Location map, coinvale link embedded for deposits, contact box, bio, faq/policies, menu of services, hours of availability by appointment only .
Nice to have
• An interactive calander where I could post dates that I am available, preferred providers for other beauty services where i could list other websites for make up and other beauty related referrals. a bridal tab would be nice to offer information about bridal services and policies.

```html
<!DOCTYPE html>
<html lang="en">
<head>
<meta charset="utf-8">
<title>Danemere Curls</title>
<link rel="stylesheet" href="https://fonts.googleapis.com/css2?family=Roboto:ital,wght@0,300;0,400;0,500;0,700;1,300;1,400;1,700&display=swap">
<style>
  :root {
    --charcoal: #474747;
    --mid-gray: #919191;
    --light-gray: #d3d3d3;
    --black: #000000;
    --night: #222222;
    --slate: #555555;
    --contact-gray: #666666;
    --white: #ffffff;
    --gold: #c9a646;
  }
  * { box-sizing: border-box; margin: 0; padding: 0; }
  html, body { width: 1200px; height: 2962px; overflow: hidden; }
  body { position: relative; font-family: "Roboto", Arial, sans-serif; background: var(--white); color: var(--charcoal); }
  h1, h2, h3 { font-weight: inherit; }
  a { text-decoration: none; color: inherit; }
  .btn { position: absolute; display: flex; align-items: center; justify-content: center; }

  /* Hero */
  .hero { position: absolute; left: 0; top: 0; width: 1200px; height: 683px; background: linear-gradient(90deg, #e9e9e9 0%, #f3f3f3 40%, #f9f9f9 100%); overflow: hidden; }
  .hero-photo { position: absolute; left: 92px; top: 70px; width: 554px; height: 613px;
    background:
      radial-gradient(ellipse 26% 20% at 48% 26%, #2c2c2c 0%, rgba(44,44,44,0) 100%),
      radial-gradient(ellipse 60% 55% at 50% 80%, #7a7a7a 0%, #5b5b5b 55%, rgba(91,91,91,0) 100%);
  }
  .brand { position: absolute; left: 430px; top: 16px; width: 340px; text-align: center; }
  .brand-mark { width: 127px; height: 127px; border-radius: 50%; background: var(--gold); margin: 0 auto; }
  .brand-name { font-weight: 300; color: var(--gold); font-size: 36px; letter-spacing: 6px; margin-top: 16px; line-height: 38px; }
  .brand-sub { font-weight: 300; color: var(--gold); font-size: 17px; letter-spacing: 14px; line-height: 22px; margin-top: 4px; }
  .main-nav a { position: absolute; top: 90px; font-size: 16px; font-weight: 500; color: #8a8a8a; white-space: nowrap; }
  .main-nav .active { color: var(--black); }
  .nav-dot { position: absolute; left: 793px; top: 114px; width: 9px; height: 9px; border-radius: 50%; background: var(--night); }
  .hero-title { position: absolute; left: 597px; width: 520px; top: 294px; text-align: center; font-size: 66px; font-weight: 700; color: var(--slate); line-height: 80px; }
  .hero-text { position: absolute; left: 597px; width: 520px; top: 378px; text-align: center; font-size: 27px; font-weight: 300; line-height: 34px; color: #b5b5b5; }
  .hero-btn { left: 757px; top: 529px; width: 213px; height: 41px; background: var(--slate); color: var(--white); font-size: 21px; font-weight: 500; }

  /* Intro band */
  .intro { position: absolute; left: 0; top: 683px; width: 1200px; height: 235px; background: var(--night); }
  .intro-text { position: absolute; left: 200px; width: 800px; top: 52px; text-align: center; color: var(--white); font-size: 20px; font-weight: 500; line-height: 27px; }
  .intro-btn { left: 498px; top: 151px; width: 205px; height: 41px; border: 3px solid var(--white); color: var(--white); font-size: 21px; font-weight: 500; }

  /* Looks grid */
  .look { position: absolute; width: 600px; }
  .look-a { left: 0; top: 918px; height: 488px; background:
      radial-gradient(ellipse 30% 32% at 30% 38%, #b8b8b8 0%, rgba(150,150,150,0) 100%),
      linear-gradient(120deg, #7e7e7e 0%, #565656 45%, #3a3a3a 100%); }
  .look-a-shade { position: absolute; left: 330px; top: 918px; width: 270px; height: 488px; background: linear-gradient(90deg, rgba(40,40,40,0) 0%, rgba(40,40,40,0.75) 30%, rgba(40,40,40,0.85) 100%); }
  .look-b { left: 600px; top: 918px; height: 488px; background:
      radial-gradient(ellipse 26% 34% at 63% 50%, #2a2a2a 0%, rgba(42,42,42,0) 100%),
      linear-gradient(180deg, #5a5a5a 0%, #4a4a4a 100%); }
  .look-c { left: 0; top: 1406px; height: 488px; background:
      radial-gradient(ellipse 24% 30% at 50% 40%, #5a5a5a 0%, rgba(60,60,60,0) 100%),
      linear-gradient(180deg, #1e1e1e 0%, #141414 100%); }
  .look-d { left: 600px; top: 1406px; height: 488px; background:
      radial-gradient(ellipse 28% 32% at 52% 50%, #a2a2a2 0%, rgba(120,120,120,0) 100%),
      linear-gradient(180deg, #333 0%, #242424 100%); }
  .service-card { position: absolute; left: 360px; top: 1004px; width: 208px; text-align: right; }
  .service-title { font-size: 52px; font-weight: 700; color: var(--white); line-height: 60px; }
  .service-text { font-size: 18px; color: #9c9c9c; line-height: 21px; margin-top: 6px; }
  .service-meta { font-size: 17px; color: #bdbdbd; margin-top: 22px; }
  .service-meta span { margin-left: 24px; }
  .service-btn { left: 428px; top: 1243px; width: 140px; height: 49px; background: var(--slate); color: var(--white); font-size: 21px; }

  /* Recommendations */
  .reviews { position: absolute; left: 304px; top: 1946px; width: 592px; }
  .review { height: 117px; border-bottom: 1px dashed #bbbbbb; padding-left: 24px; padding-top: 2px; }
  .review:last-child { border-bottom: none; }
  .review-date { font-size: 10px; color: #666; line-height: 14px; }
  .review-title { font-size: 17px; font-weight: 400; color: #333; line-height: 24px; margin-top: 3px; }
  .review-body { font-size: 12px; font-style: italic; font-weight: 300; color: #555; line-height: 17px; margin-top: 2px; width: 540px; }
  .review-btn { left: 437px; top: 2290px; width: 326px; height: 36px; background: var(--slate); color: var(--white); font-size: 21px; gap: 10px; }

  /* Contact */
  .contact { position: absolute; left: 0; top: 2388px; width: 1200px; height: 395px; background: var(--contact-gray); }
  .contact-title { position: absolute; left: 74px; top: 27px; font-size: 26px; font-weight: 700; color: var(--white); }
  .field { position: absolute; left: 74px; width: 369px; border: 3px solid var(--white); color: var(--white); font-size: 18px; font-style: italic; padding: 4px 8px; }
  .field-name { top: 82px; height: 39px; }
  .field-message { top: 140px; height: 121px; }
  .send-btn { left: 74px; top: 279px; width: 98px; height: 37px; border: 3px solid var(--white); color: var(--white); font-size: 19px; font-weight: 700; font-style: italic; }
  .contact-line { position: absolute; left: 494px; display: flex; align-items: flex-start; gap: 14px; color: var(--white); font-size: 18px; line-height: 22px; }
  .map { position: absolute; left: 705px; top: 31px; width: 413px; height: 326px; border: 3px solid #333;
    background: linear-gradient(135deg, #e6e2d6 0%, #dcdacb 50%, #d2d8c9 100%); }
  .to-top { position: absolute; left: 1140px; top: 2743px; width: 41px; height: 39px; background: #dddddd; }

  /* Footer */
  .site-footer { position: absolute; left: 0; top: 2783px; width: 1200px; height: 179px; background: var(--night); }
  .footer-brand { position: absolute; left: 499px; top: 40px; width: 200px; text-align: center; color: #dddddd; }
  .footer-mark { width: 49px; height: 49px; border-radius: 50%; background: #dddddd; margin: 0 auto; }
  .footer-name { font-weight: 300; font-size: 15px; letter-spacing: 2px; margin-top: 6px; line-height: 17px; }
  .footer-sub { font-weight: 300; font-size: 9px; letter-spacing: 6px; line-height: 12px; }
  .social { position: absolute; top: 44px; right: 74px; display: flex; gap: 14px; color: #cfcfcf; font-size: 11px; }
  .social a { display: flex; align-items: center; gap: 5px; }
  .social i { display: inline-block; width: 20px; height: 20px; border: 1.5px solid #cfcfcf; border-radius: 50%; }
  .copyright { position: absolute; left: 74px; top: 156px; font-size: 9px; color: #bbbbbb; }
</style>
</head>
<body>

<header class="hero">
  <div class="hero-photo" role="img" aria-label="Black and white portrait of the stylist in a camouflage shirt"></div>
  <div class="brand">
    <div class="brand-mark"></div>
    <div class="brand-name">DANEMERE</div>
    <div class="brand-sub">CURLS</div>
  </div>
  <nav class="main-nav" aria-label="Main">
    <a class="active" style="left:773px">HOME</a>
    <a style="left:851px">ABOUT</a>
    <a style="left:933px">SERVICES</a>
    <a style="left:1033px">CONTACT</a>
  </nav>
  <span class="nav-dot"></span>
  <h1 class="hero-title">BE THE BOSS</h1>
  <p class="hero-text">Lorem ipsum dolor sit amet, consecte-<br>tur adipisicing elit, sed do eiusmod<br>tempor incididunt ut labore et dolore<br>magna aliqua.</p>
  <a class="btn hero-btn">Learn more</a>
</header>

<section class="intro">
  <p class="intro-text">Ut vitae lectus in metus congue posuere eu at lacus. Aliquam sollicitudin<br>arcu eu ligula rhoncus, vel euismod orci cursus. Quisque eu risus at purus<br>varius congue at nec enim.</p>
  <a class="btn intro-btn">Learn more</a>
</section>

<section aria-label="Looks">
  <div class="look look-a" role="img" aria-label="Black and white photo of a woman with voluminous curly hair"></div>
  <div class="look-a-shade"></div>
  <div class="look look-b" role="img" aria-label="Black and white profile photo of a woman with a spiked short hairstyle"></div>
  <div class="look look-c" role="img" aria-label="Dark photo of a woman with long wavy hair"></div>
  <div class="look look-d" role="img" aria-label="Photo of a smiling woman with long straight hair"></div>
  <div class="service-card">
    <h2 class="service-title">Hair</h2>
    <p class="service-text">Lorem ipsum dolor sit<br>amet, consectetur<br>adipiscing elit. Ut in eros<br>placerat, pulvinar lacus<br>ac, iaculis urna.</p>
    <p class="service-meta">1h<span>$ 99.99</span></p>
  </div>
  <a class="btn service-btn">Get Look</a>
</section>

<section class="reviews" aria-label="Recommendations">
  <article class="review">
    <div class="review-date">June 23, 2018</div>
    <h3 class="review-title">Lorem Ipsum.</h3>
    <p class="review-body">"Lorem ipsum dolor sit amet, consectetur adipiscing elit. Duis in venenatis arcu. Donec et sapien nisl. Donec posuere dolor ut ipsum tempor fermentum. Integer posuere lacinia blandit. Praesent ac molestie elit, et accumsan sapien. Mauris tincidunt, erat vel molestie commodo."</p>
  </article>
  <article class="review">
    <div class="review-date">June 23, 2018</div>
    <h3 class="review-title">Lorem Ipsum.</h3>
    <p class="review-body">"Lorem ipsum dolor sit amet, consectetur adipiscing elit. Duis in venenatis arcu. Donec et sapien nisl. Donec posuere dolor ut ipsum tempor fermentum. Integer posuere lacinia blandit. Praesent ac molestie elit, et accumsan sapien. Mauris tincidunt, erat vel molestie commodo."</p>
  </article>
  <article class="review">
    <div class="review-date">June 23, 2018</div>
    <h3 class="review-title">Lorem Ipsum.</h3>
    <p class="review-body">"Lorem ipsum dolor sit amet, consectetur adipiscing elit. Duis in venenatis arcu. Donec et sapien nisl. Donec posuere dolor ut ipsum tempor fermentum. Integer posuere lacinia blandit. Praesent ac molestie elit, et accumsan sapien. Mauris tincidunt, erat vel molestie commodo."</p>
  </article>
</section>
<a class="btn review-btn">
  <svg width="20" height="20" viewBox="0 0 24 24" aria-hidden="true"><path fill="#fff" d="M12 2l2.9 6.6 7.1.6-5.4 4.7 1.6 7-6.2-3.8-6.2 3.8 1.6-7L2 9.2l7.1-.6z"/></svg>
  Write a Recomandation
</a>

<section class="contact">
  <h2 class="contact-title">Get In Touch</h2>
  <div class="field field-name">Full Name</div>
  <div class="field field-message">Message</div>
  <a class="btn send-btn">Send</a>
  <div class="contact-line" style="top:96px">
    <svg width="20" height="24" viewBox="0 0 20 24" aria-hidden="true"><path fill="#fff" d="M10 0C4.8 0 1 3.9 1 9c0 6.5 9 15 9 15s9-8.5 9-15c0-5.1-3.8-9-9-9zm0 12.5A3.5 3.5 0 1 1 10 5.5a3.5 3.5 0 0 1 0 7z"/></svg>
    <span>1234 Lantern Road<br>12 - Halvern - TX</span>
  </div>
  <div class="contact-line" style="top:151px">
    <svg width="22" height="22" viewBox="0 0 24 24" aria-hidden="true"><circle cx="12" cy="12" r="12" fill="#fff"/><path fill="#666" d="M8.2 5.5l2 3.3-1.4 1.5c.8 1.8 2.2 3.2 4 4l1.5-1.4 3.3 2-.9 2.6c-5.2-.2-9.5-4.5-9.7-9.7z"/></svg>
    <span>1.23.456.7890</span>
  </div>
  <div class="map" role="img" aria-label="Street map with a pin marking the salon location"></div>
</section>
<a class="to-top" aria-label="Back to top">
  <svg width="41" height="39" viewBox="0 0 41 39" aria-hidden="true"><path d="M13 23l7.5-7.5L28 23" fill="none" stroke="#333" stroke-width="3.5"/></svg>
</a>

<footer class="site-footer">
  <div class="footer-brand">
    <div class="footer-mark"></div>
    <div class="footer-name">DANEMERE</div>
    <div class="footer-sub">CURLS</div>
  </div>
  <div class="social">
    <a><i></i>Tubely</a>
    <a><i></i>Friendly</a>
    <a><i></i>Chirper</a>
  </div>
  <p class="copyright">Copyright © 2016 All rights reserved.</p>
</footer>

</body>
</html>
```